Fatigued and Overloaded by COVID Messages? We need original illustrations to show that.

Everywhere you look there are messages about COVID. That is leading many people to feel fatigued and overloaded by the messages.

We surveyed U.S. adults March 20th - 24th, 2020 and measured message fatigue, information overload, perceived repetition, and perceived exaggeration. Here is how participants responded:

When it comes to coronavirus . . .
55% feel exhausted by all the messages.
54% feel overloaded by the amount of information.
51% feel that the messages are repetitive.
47% feel like messages exaggerate how bad it is.

In other words, almost half of U.S. adults show signs of message fatigue, information overload, perceived message repetition, and perceived message exaggeration.

We will continue to survey 400 adults every week for the next 16 weeks. Each time we will measure message fatigue, information overload, perceived repetition, and perceived exaggeration. We expect that it will increase over time.

What are we looking for? We need innovative and original illustrations that attempt to communicate these findings. The illustrations would visualize message fatigue, information overload, perceived message repetition, and perceived message exaggeration.

What sort of visual are we looking for? Our preference is for an original illustration (or set of illustrations). Our preference is for creative and powerful illustrations, but we are also open to the creative and well-executed infographics.

We need these images fast . We will award monetary prizes to the 3 best designs. If we like more than that, then we might purchase more (e.g., in past contests, we have purchased as many as 30 designs).

What we will need:
(1) The illustrations must be original and we will need the photoshop and/or illustrator files for all artwork. (By original, we mean that the illustrations are 100% created by you. Our organization requires that we utilize only original illustrated work. We have had issues with free imagery being pirated and reposted as free. We sidestep that issue by just having everything created.)

(2) The illustration should say, somewhere: "Based on a survey of 400 U.S. adults conducted March 20 - 24th, 2020."

(3) We will have almost 4 months worth of data by the time this is done. In other words, the illustrations might be able to help us present that weekly data.

(4) We have conducted other Artvendo projects. It might be helpful to examine designs we liked in the past. For example, here is another COVID project we just finished:

https://jobs.artvendo-example.com/job/5162048

Target Market(s)

U.S. adults

Requirements
Must have
• Original illustrations. Mobile friendly design. People will view this on their smartphones.
Nice to have
• A design that we can use to communicate the data across time.

```html
<!DOCTYPE html>
<html lang="en">
<head>
<meta charset="utf-8">
<title>Information Overload – 54%</title>
<link rel="stylesheet" href="https://fonts.googleapis.com/css2?family=Fira+Sans:wght@500&family=Fira+Sans+Condensed:ital,wght@1,400;1,500&display=swap">
<style>
  :root {
    --slate: #465059;
    --ground: #32383f;
    --word: #dcdcdc;
    --accent: #f39c36;
    --figure-grey: #8f9296;
    --figure-orange: #e8902e;
    --figure-pants: #2b4448;
  }
  html, body {
    margin: 0;
    padding: 0;
    width: 1200px;
    height: 1200px;
    overflow: hidden;
    background: var(--slate);
  }
  .poster {
    position: relative;
    width: 1200px;
    height: 1200px;
    overflow: hidden;
    background: var(--slate);
  }
  .word-rain {
    position: absolute;
    left: 0;
    top: 0;
    width: 1200px;
    height: 1007px;
  }
  .word-column {
    position: absolute;
    left: calc(var(--x) * 1px);
    width: calc(var(--s) * 1px);
    font-size: calc(var(--s) * 1px);
    overflow: hidden;
    display: flex;
    flex-direction: column;
    justify-content: flex-end;
    align-items: center;
    font-family: "Fira Sans Condensed", "Arial Narrow", sans-serif;
    font-style: italic;
    font-weight: 500;
    color: var(--word);
  }
  .word-column span {
    writing-mode: vertical-rl;
    white-space: nowrap;
    line-height: 1;
  }
  .word-column--full { top: 0; height: 1007px; }
  .word-column--above-walker { top: 0; height: 470px; }
  .word-column--between { top: 292px; height: 178px; }
  .word-column--below-stat { top: 292px; height: 715px; }

  .stat {
    position: absolute;
    left: 650px;
    top: 42px;
    margin: 0;
    font-family: "Fira Sans", "Helvetica Neue", Arial, sans-serif;
    font-size: 272px;
    font-weight: 500;
    line-height: 1;
    letter-spacing: -0.01em;
    color: var(--accent);
  }
  .walker {
    position: absolute;
    left: 438px;
    top: 475px;
    width: 298px;
    height: 547px;
  }
  .ground {
    position: absolute;
    left: 0;
    right: 0;
    bottom: 0;
    height: 193px;
    background: var(--ground);
  }
  .headline {
    position: absolute;
    margin: 0;
    font-family: "Fira Sans Condensed", "Arial Narrow", sans-serif;
    font-style: italic;
    font-weight: 400;
    font-size: 113px;
    line-height: 1;
    color: var(--accent);
    white-space: nowrap;
  }
  .headline--first { left: 186px; top: 1018px; }
  .headline--second { left: 615px; top: 1082px; }
</style>
</head>
<body>
<main class="poster">
  <div class="word-rain" aria-hidden="true">
    <!-- left field -->
    <div class="word-column word-column--full" style="--x:0;--s:14"><span>coronavirus coronavirus coronavirus coronavirus coronavirus coronavirus coronavirus coronavirus coronavirus coronavirus coronavirus coronavirus coronavirus coronavirus coronavirus coronavirus</span></div>
    <div class="word-column word-column--full" style="--x:16;--s:70"><span>coronavirus coronavirus coronavirus coronavirus</span></div>
    <div class="word-column word-column--full" style="--x:88;--s:12"><span>coronavirus coronavirus coronavirus coronavirus coronavirus coronavirus coronavirus coronavirus coronavirus coronavirus coronavirus</span></div>
    <div class="word-column word-column--full" style="--x:102;--s:24"><span>coronavirus coronavirus coronavirus coronavirus coronavirus coronavirus coronavirus coronavirus coronavirus</span></div>
    <div class="word-column word-column--full" style="--x:128;--s:48"><span>coronavirus coronavirus coronavirus coronavirus coronavirus</span></div>
    <div class="word-column word-column--full" style="--x:178;--s:12"><span>coronavirus coronavirus coronavirus coronavirus coronavirus coronavirus coronavirus coronavirus coronavirus coronavirus coronavirus coronavirus coronavirus coronavirus coronavirus coronavirus coronavirus coronavirus</span></div>
    <div class="word-column word-column--full" style="--x:192;--s:14"><span>coronavirus coronavirus coronavirus coronavirus coronavirus coronavirus coronavirus coronavirus coronavirus coronavirus</span></div>
    <div class="word-column word-column--full" style="--x:208;--s:40"><span>coronavirus coronavirus coronavirus coronavirus coronavirus coronavirus</span></div>
    <div class="word-column word-column--full" style="--x:250;--s:10"><span>coronavirus coronavirus coronavirus coronavirus coronavirus coronavirus coronavirus coronavirus coronavirus coronavirus coronavirus coronavirus</span></div>
    <div class="word-column word-column--full" style="--x:262;--s:30"><span>coronavirus coronavirus coronavirus coronavirus coronavirus coronavirus coronavirus coronavirus</span></div>
    <div class="word-column word-column--full" style="--x:294;--s:22"><span>coronavirus coronavirus coronavirus coronavirus coronavirus coronavirus coronavirus coronavirus coronavirus coronavirus</span></div>
    <div class="word-column word-column--full" style="--x:318;--s:36"><span>coronavirus coronavirus coronavirus coronavirus coronavirus coronavirus</span></div>
    <div class="word-column word-column--full" style="--x:356;--s:14"><span>coronavirus coronavirus coronavirus coronavirus coronavirus coronavirus coronavirus coronavirus coronavirus coronavirus coronavirus coronavirus</span></div>
    <div class="word-column word-column--full" style="--x:372;--s:24"><span>coronavirus coronavirus coronavirus coronavirus coronavirus coronavirus coronavirus coronavirus coronavirus</span></div>
    <div class="word-column word-column--full" style="--x:398;--s:34"><span>coronavirus coronavirus coronavirus coronavirus coronavirus coronavirus coronavirus</span></div>

    <!-- above the walker -->
    <div class="word-column word-column--above-walker" style="--x:438;--s:16"><span>coronavirus coronavirus coronavirus coronavirus coronavirus coronavirus</span></div>
    <div class="word-column word-column--above-walker" style="--x:456;--s:30"><span>coronavirus coronavirus coronavirus coronavirus</span></div>
    <div class="word-column word-column--above-walker" style="--x:488;--s:12"><span>coronavirus coronavirus coronavirus coronavirus coronavirus</span></div>
    <div class="word-column word-column--above-walker" style="--x:502;--s:40"><span>coronavirus coronavirus coronavirus</span></div>
    <div class="word-column word-column--above-walker" style="--x:544;--s:14"><span>coronavirus coronavirus coronavirus coronavirus coronavirus coronavirus</span></div>
    <div class="word-column word-column--above-walker" style="--x:560;--s:24"><span>coronavirus coronavirus coronavirus coronavirus</span></div>
    <div class="word-column word-column--above-walker" style="--x:586;--s:46"><span>coronavirus coronavirus coronavirus</span></div>
    <div class="word-column word-column--above-walker" style="--x:634;--s:12"><span>coronavirus coronavirus coronavirus coronavirus coronavirus coronavirus coronavirus</span></div>

    <!-- between stat and walker -->
    <div class="word-column word-column--between" style="--x:648;--s:12"><span>coronavirus coronavirus coronavirus</span></div>
    <div class="word-column word-column--between" style="--x:662;--s:26"><span>coronavirus</span></div>
    <div class="word-column word-column--between" style="--x:690;--s:10"><span>coronavirus coronavirus coronavirus</span></div>
    <div class="word-column word-column--between" style="--x:702;--s:20"><span>coronavirus coronavirus</span></div>
    <div class="word-column word-column--between" style="--x:724;--s:12"><span>coronavirus coronavirus</span></div>

    <!-- below the stat -->
    <div class="word-column word-column--below-stat" style="--x:738;--s:18"><span>coronavirus coronavirus coronavirus coronavirus coronavirus coronavirus coronavirus coronavirus</span></div>
    <div class="word-column word-column--below-stat" style="--x:757;--s:40"><span>coronavirus coronavirus coronavirus coronavirus</span></div>
    <div class="word-column word-column--below-stat" style="--x:798;--s:12"><span>coronavirus coronavirus coronavirus coronavirus coronavirus coronavirus coronavirus coronavirus coronavirus coronavirus coronavirus</span></div>
    <div class="word-column word-column--below-stat" style="--x:811;--s:30"><span>coronavirus coronavirus coronavirus coronavirus coronavirus</span></div>
    <div class="word-column word-column--below-stat" style="--x:842;--s:48"><span>coronavirus coronavirus coronavirus</span></div>
    <div class="word-column word-column--below-stat" style="--x:891;--s:14"><span>coronavirus coronavirus coronavirus coronavirus coronavirus coronavirus coronavirus coronavirus coronavirus coronavirus</span></div>
    <div class="word-column word-column--below-stat" style="--x:906;--s:22"><span>coronavirus coronavirus coronavirus coronavirus coronavirus coronavirus coronavirus</span></div>
    <div class="word-column word-column--below-stat" style="--x:929;--s:36"><span>coronavirus coronavirus coronavirus coronavirus</span></div>
    <div class="word-column word-column--below-stat" style="--x:966;--s:12"><span>coronavirus coronavirus coronavirus coronavirus coronavirus coronavirus coronavirus coronavirus coronavirus coronavirus coronavirus coronavirus</span></div>
    <div class="word-column word-column--below-stat" style="--x:979;--s:72"><span>coronavirus coronavirus coronavirus</span></div>
    <div class="word-column word-column--below-stat" style="--x:1052;--s:16"><span>coronavirus coronavirus coronavirus coronavirus coronavirus coronavirus coronavirus coronavirus coronavirus</span></div>
    <div class="word-column word-column--below-stat" style="--x:1069;--s:26"><span>coronavirus coronavirus coronavirus coronavirus coronavirus coronavirus</span></div>
    <div class="word-column word-column--below-stat" style="--x:1096;--s:14"><span>coronavirus coronavirus coronavirus coronavirus coronavirus coronavirus coronavirus coronavirus coronavirus coronavirus</span></div>
    <div class="word-column word-column--below-stat" style="--x:1111;--s:34"><span>coronavirus coronavirus coronavirus coronavirus coronavirus</span></div>

    <!-- right edge -->
    <div class="word-column word-column--full" style="--x:1148;--s:12"><span>coronavirus coronavirus coronavirus coronavirus coronavirus coronavirus coronavirus coronavirus coronavirus coronavirus coronavirus coronavirus coronavirus coronavirus coronavirus coronavirus coronavirus coronavirus coronavirus coronavirus</span></div>
    <div class="word-column word-column--full" style="--x:1162;--s:14"><span>coronavirus coronavirus coronavirus coronavirus coronavirus coronavirus coronavirus coronavirus coronavirus coronavirus coronavirus coronavirus coronavirus coronavirus coronavirus coronavirus</span></div>
    <div class="word-column word-column--full" style="--x:1178;--s:22"><span>coronavirus coronavirus coronavirus coronavirus coronavirus coronavirus coronavirus coronavirus coronavirus coronavirus</span></div>
  </div>

  <p class="stat">54%</p>

  <svg class="walker" viewBox="0 0 298 547" role="img" aria-label="Illustration of a person in a grey hoodie, dark track pants and a blue backpack walking head down under an orange umbrella">
    <defs>
      <linearGradient id="walker-tone" x1="0" y1="0" x2="0" y2="1">
        <stop offset="0" stop-color="var(--figure-orange)"/>
        <stop offset="0.35" stop-color="var(--figure-orange)"/>
        <stop offset="0.5" stop-color="var(--figure-grey)"/>
        <stop offset="1" stop-color="var(--figure-pants)"/>
      </linearGradient>
    </defs>
    <rect width="298" height="547" fill="url(#walker-tone)"/>
  </svg>

  <div class="ground"></div>
  <h1 class="headline headline--first">information</h1>
  <p class="headline headline--second">overload</p>
</main>
</body>
</html>
```